Welland Dental, P.C. New stationary and business card for modern Dental Office

We need a new stationary/envelope/business card design using our newly designed logo. We are looking for an upscale look. Our new logo is used on our signage, using black as the background and white for the lettering. We would like the stationary to have black, white, possible greys or silver. We are looking for a letterhead, envelope, and business card design for three different employees, as well as a 4th card, same design, but just general with no employee name.
Updates

Project Deadline Extended
Reason: We began this project in the middle of our move into our new office. Things got pretty hectic and we just didn't have the time to go through designs. We now settled in and finally eliminated the designs that didn't work for us. We would like to extend the project another 5 days, and then finalize our decision. Most of the submissions showed business cards alone, with no stationary designs. Our original request was for stationary and business cards. Please keep this in mind.

Target Market(s)

Dental patients expecting high quality, cosmetic dentistry

Industry/Entity Type

Business

Contact Information for Business Card

Will need a design using our logo. All cards will be the same, other than that one card will have Office Managers name, One for the Doctor, Hygienist,
1. Office Manager - Marisol Penrose
2. Hygienist - Courtney Whitlock
3. Owen T. Welland, D.D.S.
4. One general one with no staff names

Font styles to use
Other font styles liked:
• see upload

Colors
000000
1b1b1b
757575
c9c9c9
e8e8e8
ffffff

Requirements
Must have
• -Logo
• -Phone number (718)555-0143
• -Address: 4392 63rd Ave
• Lower Level
• Brooklyn, NY 11398

```html
<!DOCTYPE html>
<html lang="en">
<head>
<meta charset="utf-8">
<title>Welland Dental, P.C. — Letterhead</title>
<link rel="stylesheet" href="https://fonts.googleapis.com/css2?family=Tinos&display=swap">
<style>
  :root {
    --ink: #000000;
    --ink-soft: #1b1b1b;
    --grey: #757575;
    --paper: #ffffff;
  }
  html, body {
    margin: 0;
    padding: 0;
    overflow: hidden;
    background: var(--paper);
  }
  .letterhead {
    position: relative;
    width: 928px;
    height: 1200px;
    background: var(--paper);
    overflow: hidden;
    font-family: "Tinos", "Times New Roman", serif;
  }
  .address {
    position: absolute;
    left: 71px;
    top: 66px;
    margin: 0;
    font-style: normal;
    font-size: 17px;
    line-height: 24px;
    letter-spacing: 1.6px;
    color: var(--ink-soft);
  }
  .rule-row {
    position: absolute;
    top: 176px;
    height: 2px;
  }
  .rule-row--dark { left: 70px; width: 312px; background: var(--ink-soft); }
  .rule-row--grey { left: 397px; width: 88px; background: var(--grey); height: 1.5px; }
  .rule-row--dark-short { left: 500px; width: 78px; background: var(--ink-soft); }
  .brand-name {
    position: absolute;
    right: 48px;
    top: 122px;
    margin: 0;
    font-family: "Tinos", "Times New Roman", serif;
    font-weight: 400;
    font-size: 28px;
    line-height: 34px;
    letter-spacing: 2px;
    color: var(--ink-soft);
    white-space: nowrap;
  }
  .footer-band {
    position: absolute;
    left: 53px;
    width: 836px;
  }
  .footer-band--grey { top: 1090px; height: 5px; background: var(--grey); }
  .footer-band--dark { top: 1103px; height: 3px; background: var(--ink-soft); }
</style>
</head>
<body>
  <main class="letterhead">
    <address class="address">
      4392 63rd Ave<br>
      Lower Level<br>
      Brooklyn, NY 11398<br>
      (718)555-0143
    </address>

    <div class="rule-row rule-row--dark"></div>
    <div class="rule-row rule-row--grey"></div>
    <div class="rule-row rule-row--dark-short"></div>

    <p class="brand-name">Welland Dental, P.C.</p>

    <div class="footer-band footer-band--grey"></div>
    <div class="footer-band footer-band--dark"></div>
  </main>
</body>
</html>
```